Business Card Design - Corporate

Create a sleek elegant business card layout while suggesting a color scheme. Convey cutting edge technology while maintaining a corporate feel that is easily readable.

Company designs and manufactures consumer electronic products for mass retail that are mainly app driven.

(vector logo and die-line provided)

Target Market(s)

Corporate level, tech industry.

Industry/Entity Type

Business

Contact Information for Business Card

Generic Info:

Name
Title
email
address
phone 1
phone 2
website (quillbarn.com) on back

Font styles to use
Sans Serif

Requirements
Must have
• At least 2 colors + white on one side.
Nice to have
• Solid suggestion on color for logo and overall design. Color flood on back of card.
Should not have
• background texture like... marble, stone, patterns or circuit boards

```html
<!DOCTYPE html>
<html lang="en">
<head>
<meta charset="utf-8">
<title>Quillbarn Business Card</title>
<link href="https://fonts.googleapis.com/css2?family=Open+Sans:wght@400;600;700&display=swap" rel="stylesheet">
<style>
  :root {
    --backdrop: #ababab;
    --card-front: #ffffff;
    --card-back: #5d5d5d;
    --ink-dark: #4a4a4a;
    --ink-light: #ffffff;
    --accent-blue: #1d6fc2;
  }
  * { margin: 0; padding: 0; box-sizing: border-box; }
  html, body {
    width: 1200px; height: 900px; overflow: hidden;
    background: var(--backdrop);
    font-family: "Open Sans", sans-serif;
  }
  .stage { position: relative; width: 1200px; height: 900px; }
  .card {
    position: absolute; top: 215px;
    width: 414px; height: 414px; border-radius: 50%;
  }
  .card-front { left: 164px; background: var(--card-front); }
  .card-back { left: 623px; background: var(--card-back); color: var(--ink-light); text-align: center; }

  .brand-name {
    position: absolute; left: 0; right: 0; top: 177px;
    text-align: center;
    font-size: 46px; font-weight: 600; letter-spacing: 6px;
    color: var(--ink-dark);
  }
  .web-address {
    position: absolute; left: 0; right: 0; top: 304px;
    text-align: center;
    font-size: 20px; font-weight: 700; letter-spacing: 1.8px;
    color: var(--ink-dark);
  }
  .web-address .domain { color: var(--accent-blue); }

  .holder-name {
    position: absolute; left: 0; right: 0; top: 80px;
    font-size: 20px; font-weight: 700;
  }
  .holder-title {
    position: absolute; left: 0; right: 0; top: 113px;
    font-size: 17px; font-weight: 400;
  }
  .contact-list {
    position: absolute; left: 0; right: 0; top: 176px;
    list-style: none; font-size: 17px;
  }
  .contact-list li {
    height: 28px; display: flex; align-items: center; justify-content: center; gap: 7px;
  }
  .contact-list svg { fill: var(--ink-light); }
  .address {
    position: absolute; left: 0; right: 0; top: 290px;
    font-size: 17px; line-height: 24px; font-style: normal;
  }
</style>
</head>
<body>
<main class="stage">
  <section class="card card-front">
    <div class="brand-name">QUILLBARN</div>
    <div class="web-address">WWW.<span class="domain">QUILLBARN</span>.COM</div>
  </section>

  <section class="card card-back">
    <h1 class="holder-name">JONATHAN MERCER</h1>
    <p class="holder-title">Managing Director</p>
    <ul class="contact-list">
      <li>
        <svg width="16" height="18" viewBox="0 0 24 24" aria-hidden="true"><path d="M6.6 10.8c1.4 2.8 3.8 5.1 6.6 6.6l2.2-2.2c.3-.3.7-.4 1-.2 1.1.4 2.3.6 3.6.6.6 0 1 .4 1 1V20c0 .6-.4 1-1 1C10.6 21 3 13.4 3 4c0-.6.4-1 1-1h3.5c.6 0 1 .4 1 1 0 1.3.2 2.5.6 3.6.1.3 0 .7-.2 1z"/></svg>
        555-2468-100
      </li>
      <li>
        <svg width="16" height="18" viewBox="0 0 24 24" aria-hidden="true"><path d="M6.6 10.8c1.4 2.8 3.8 5.1 6.6 6.6l2.2-2.2c.3-.3.7-.4 1-.2 1.1.4 2.3.6 3.6.6.6 0 1 .4 1 1V20c0 .6-.4 1-1 1C10.6 21 3 13.4 3 4c0-.6.4-1 1-1h3.5c.6 0 1 .4 1 1 0 1.3.2 2.5.6 3.6.1.3 0 .7-.2 1z"/></svg>
        555-2468-101
      </li>
      <li>
        <svg width="16" height="12" viewBox="0 0 16 12" aria-hidden="true"><path d="M0 0h16v12H0z M1.5 1.5v9h13v-9L8 6.5z M2.5 1.5L8 5.5l5.5-4z" fill-rule="evenodd"/></svg>
        hello@mailbox.com
      </li>
    </ul>
    <address class="address">Street Line Goes Here,<br>Location Postcode 60318</address>
  </section>
</main>
</body>
</html>
```